Business Card Design for Varnor Facility Services

We are looking for a Business Card Design for the Company "Varnor Facility Services."
Front side:
- Company Logo (small)
- Company Name, address, pohone, website and personal data.
- white background, for text e.g. company colors (blue or green like in the logo)
Please use following data:
Company data:
Varnor Facility Services Kuttelbrand
Lindauweg 14
6330 Cham
www.varnor-fs.example
Person data:
Tobias Kuttelbrand
Geschäftsführer
+41 76 915 47 18
info@varnor-fs.example
Back side:
could be colored in blue or green
please use a big logo sing and some smaller icons to say what is all beeing offered in facility services, like cleaning, maintenance cleaning
industrial cleaning, caretaking, gardening, disposal. There is no need for everyone of the icons if there are similar or an icon is standing for more of them.
Cleaning Service
colors to use:
blue: HEX 246BB0
green: HEX 52B33E

```html
<!DOCTYPE html>
<html lang="de">
<head>
<meta charset="utf-8">
<title>Varnor Facility Services – Business Card</title>
<link href="https://fonts.googleapis.com/css2?family=Roboto:wght@400;500;700&display=swap" rel="stylesheet">
<style>
  :root {
    --brand-blue: #246BB0;
    --brand-green: #52B33E;
    --green-light: #8CC63F;
    --green-deep: #1FA04A;
    --paper: #FFFFFF;
    --stage: #2B2B2B;
    --rule: #246BB0;
  }
  * { box-sizing: border-box; margin: 0; padding: 0; }
  html, body {
    width: 1200px; height: 900px; overflow: hidden;
    background: var(--stage);
    font-family: "Roboto", Arial, sans-serif;
  }
  .stage {
    width: 1200px; height: 900px;
    position: relative;
  }
  .card {
    position: absolute;
    width: 640px; height: 366px;
    border-radius: 26px;
    overflow: hidden;
  }

  /* Back side */
  .card--back { left: 120px; top: 50px; }
  .back-pattern {
    position: absolute; inset: 0;
    background: linear-gradient(160deg, var(--green-light) 0%, #6DBE45 45%, var(--green-deep) 100%);
  }
  .back-content {
    position: absolute; inset: 0;
    display: flex; flex-direction: column; align-items: center; justify-content: center;
    color: var(--paper); text-align: center;
  }
  .back-brand {
    display: flex; align-items: center; gap: 14px;
    font-weight: 700; font-size: 40px; letter-spacing: 1px;
  }
  .brand-dot {
    width: 22px; height: 22px; border-radius: 50%;
    background: var(--paper);
  }
  .service-list {
    margin-top: 34px;
    font-weight: 500; font-size: 19px; line-height: 1.5;
  }
  .service-list .sep {
    display: inline-block; width: 8px; height: 8px; border: 1.5px solid var(--paper);
    border-radius: 50%; margin: 0 7px; vertical-align: middle;
  }

  /* Front side */
  .card--front { left: 440px; top: 474px; background: var(--paper); }
  .front-brand {
    position: absolute; left: 36px; top: 38px;
    display: flex; align-items: center; gap: 12px;
    color: var(--brand-blue); font-weight: 700; font-size: 26px;
  }
  .front-brand .brand-dot { width: 18px; height: 18px; background: var(--brand-green); }
  .company-block {
    position: absolute; right: 36px; top: 100px;
    text-align: right; color: var(--brand-blue);
    font-size: 15px; line-height: 1.35;
  }
  .company-name { font-weight: 700; font-size: 17px; }
  .company-web {
    margin-top: 14px; color: var(--brand-green); font-weight: 700; font-size: 16px;
  }
  .divider {
    position: absolute; left: 36px; right: 36px; top: 232px;
    border-top: 1.5px solid var(--rule);
  }
  .person {
    position: absolute; left: 36px; top: 250px;
  }
  .person-name { color: var(--brand-blue); font-weight: 700; font-size: 24px; }
  .person-role { color: var(--brand-green); font-weight: 500; font-size: 16px; margin-top: 2px; }
  .contact-list { list-style: none; margin-top: 14px; }
  .contact-item {
    display: flex; align-items: center; gap: 10px;
    color: var(--brand-blue); font-weight: 500; font-size: 16px; margin-bottom: 6px;
  }
  .contact-icon { width: 22px; height: 22px; flex: none; }
</style>
</head>
<body>
<main class="stage">

  <section class="card card--back" aria-label="Card back side">
    <div class="back-pattern" role="img" aria-label="Green background with a faint pattern of cleaning and gardening service icons"></div>
    <div class="back-content">
      <div class="back-brand"><span class="brand-dot"></span>Varnor Facility Services</div>
      <p class="service-list">
        Cleaning<span class="sep"></span>Maintenance cleaning<span class="sep"></span>Industrial cleaning<br>
        Caretaking<span class="sep"></span>Gardening<span class="sep"></span>Disposal.
      </p>
    </div>
  </section>

  <section class="card card--front" aria-label="Card front side">
    <div class="front-brand"><span class="brand-dot"></span>Varnor Facility Services</div>

    <div class="company-block">
      <p class="company-name">Varnor Facility Services Kuttelbrand</p>
      <p>Lindauweg 14</p>
      <p>6330 Cham</p>
      <p class="company-web">www.varnor-fs.example</p>
    </div>

    <div class="divider"></div>

    <div class="person">
      <p class="person-name">Tobias Kuttelbrand</p>
      <p class="person-role">Geschäftsführer</p>
      <ul class="contact-list">
        <li class="contact-item">
          <svg class="contact-icon" viewBox="0 0 24 24" aria-hidden="true">
            <circle cx="12" cy="12" r="12" fill="#52B33E"/>
            <path d="M8.2 6.5l2 2.4-1.1 1.4a7 7 0 0 0 4.6 4.6l1.4-1.1 2.4 2-1.1 1.7c-4.6 0-9.6-5-9.6-9.6z" fill="#fff"/>
          </svg>
          +41 76 915 47 18
        </li>
        <li class="contact-item">
          <svg class="contact-icon" viewBox="0 0 24 24" aria-hidden="true">
            <circle cx="12" cy="12" r="12" fill="#52B33E"/>
            <rect x="6" y="8" width="12" height="8.5" rx="1" fill="none" stroke="#fff" stroke-width="1.4"/>
            <path d="M6.3 8.4L12 13l5.7-4.6" fill="none" stroke="#fff" stroke-width="1.4"/>
          </svg>
          info@varnor-fs.example
        </li>
      </ul>
    </div>
  </section>

</main>
</body>
</html>
```